Business Card Design needed for logo design project

Our company needs a Business Card Design. Please refer to our original project in the link above.
Dorian Pellworth
Broker

W: Velvetcrestestates.example
P: 555-302-7184
F: 555-741-2096
E: dorianpellworth@mailbox.example
A: North Dallas Office
Updates

Name Spelling update , sorry Dorian Pellworth card is double sided

```html
<!DOCTYPE html>
<html lang="en">
<head>
<meta charset="utf-8">
<title>Velvetcrest Estates Realty – Business Card</title>
<link href="https://fonts.googleapis.com/css2?family=Cinzel:wght@500;600&family=Open+Sans:wght@400&display=swap" rel="stylesheet">
<style>
  :root {
    --backdrop: #1b1b1b;
    --card-black: #0a0a0a;
    --card-black-edge: #161616;
    --card-grey-light: #5a5a5a;
    --card-grey-dark: #2e2e2e;
    --gold: #c9a86a;
    --gold-soft: #b8955a;
    --text-light: #d9d9d9;
    --text-muted: #a8a8a8;
  }
  * { margin: 0; padding: 0; box-sizing: border-box; }
  html, body {
    width: 1200px; height: 1134px; overflow: hidden;
    background: var(--backdrop);
  }
  .canvas {
    position: relative; width: 1200px; height: 1134px;
  }
  .card {
    position: absolute; left: 190px; width: 820px; height: 468px;
    border-radius: 4px; box-shadow: 0 10px 30px rgba(0,0,0,.6);
    overflow: hidden;
  }
  .card--back {
    top: 66px;
    background: radial-gradient(ellipse at 40% 50%, var(--card-black-edge) 0%, var(--card-black) 70%);
  }
  .card--front {
    top: 600px;
    background: radial-gradient(ellipse at 50% 40%, var(--card-grey-light) 0%, var(--card-grey-dark) 85%);
  }
  .brand {
    position: absolute; display: flex; flex-direction: column; align-items: center;
  }
  .brand__mark {
    width: 92px; height: 92px; border-radius: 50%;
    background: var(--gold); margin-bottom: 22px;
  }
  .brand__name {
    font-family: "Cinzel", serif; font-weight: 600; color: var(--gold);
    font-size: 26px; letter-spacing: 1px; text-align: center; line-height: 1.2;
  }
  .card--back .brand { left: 60px; top: 110px; width: 330px; }
  .card--front .brand { left: 0; right: 0; top: 110px; }
  .card--front .brand__mark { width: 110px; height: 110px; }
  .card--front .brand__name { font-size: 30px; }
  .website {
    margin-top: 14px; font-family: "Open Sans", sans-serif; font-size: 20px;
    color: var(--text-light);
  }
  .contact {
    position: absolute; left: 440px; top: 132px;
  }
  .contact__name {
    font-family: "Cinzel", serif; font-weight: 600; color: var(--gold);
    font-size: 30px; letter-spacing: 1px;
  }
  .contact__role {
    font-family: "Open Sans", sans-serif; color: var(--text-muted);
    font-size: 16px; letter-spacing: 2px; margin: 2px 0 22px;
  }
  .contact__list { list-style: none; }
  .contact__item {
    display: flex; align-items: center; gap: 12px; margin-bottom: 10px;
    font-family: "Open Sans", sans-serif; font-size: 16px; color: var(--text-light);
  }
  .contact__icon { width: 14px; height: 14px; fill: var(--gold-soft); flex: none; }
</style>
</head>
<body>
<main class="canvas">
  <section class="card card--back" aria-label="Card back with contact details">
    <div class="brand">
      <div class="brand__mark"></div>
      <div class="brand__name">Velvetcrest Estates Realty</div>
    </div>
    <div class="contact">
      <h1 class="contact__name">Dorian Pellworth</h1>
      <p class="contact__role">Broker</p>
      <ul class="contact__list">
        <li class="contact__item">
          <svg class="contact__icon" viewBox="0 0 16 16"><circle cx="8" cy="8" r="7" fill="none" stroke="#b8955a" stroke-width="1.6"/><path d="M1 8h14M8 1c-3 4-3 10 0 14M8 1c3 4 3 10 0 14" fill="none" stroke="#b8955a" stroke-width="1.2"/></svg>
          Velvetcrestestates.example
        </li>
        <li class="contact__item">
          <svg class="contact__icon" viewBox="0 0 16 16"><path d="M4 1l3 3-2 2c1 2 3 4 5 5l2-2 3 3-2 3C7 15 1 9 1 4z"/></svg>
          555-302-7184
        </li>
        <li class="contact__item">
          <svg class="contact__icon" viewBox="0 0 16 16"><rect x="4" y="1" width="8" height="5"/><rect x="1" y="6" width="14" height="7" rx="1"/><rect x="4" y="11" width="8" height="4"/></svg>
          555-741-2096
        </li>
        <li class="contact__item">
          <svg class="contact__icon" viewBox="0 0 16 16"><rect x="1" y="3" width="14" height="10" rx="1"/><path d="M1 4l7 5 7-5" fill="none" stroke="#0a0a0a" stroke-width="1.3"/></svg>
          dorianpellworth@mailbox.example
        </li>
      </ul>
    </div>
  </section>

  <section class="card card--front" aria-label="Card front with brand">
    <div class="brand">
      <div class="brand__mark"></div>
      <div class="brand__name">Velvetcrest Estates Realty</div>
      <div class="website">Velvetcrestestates.example</div>
    </div>
  </section>
</main>
</body>
</html>
```